RM Cargoline businesscard project

RM Cargoline Ltd is a freshly founded small (3 employees), young (average age is 30 years) company, living from the road transportation market without own tools.
We would like to have an impressive, new-line, cool busines card for a freshly founded forwarding company on an overcrowded market which raises attention and makes the potential partners eager to work with us.

Target Market(s)

The main profile of the company is logistic/forwarding on road.

Industry/Entity Type

Freight Forwarding

Contact Information for Business Card

Name: Berki Zsófia
Title: general manager
mobile nr: +36-70/482-5193
fax nr: +36-1/534-9061
e-mail: zsofia.berki@rmcargoline.example
info@rmcargoline.example
website address: http://www.rmcargoline.example
and if possible maybe some funny or helpful info on the back

Requirements
Must have
• contact details above
Nice to have
• some really nice and catching back-side (info, graphics, useful tool info... anything)
Should not have
• trucks, road, ship, airplane on it...

```html
<!DOCTYPE html>
<html lang="en">
<head>
<meta charset="utf-8">
<title>RM Cargoline – Business Card</title>
<link href="https://fonts.googleapis.com/css2?family=Asap+Condensed:wght@500&family=Open+Sans:wght@400;600;700&display=swap" rel="stylesheet">
<style>
  :root {
    --backdrop: #2c2d31;
    --card: #ffffff;
    --ink: #2b2b2b;
    --brand-blue: #4f7fbf;
    --pale-blue: #dfe6f1;
  }
  * { box-sizing: border-box; margin: 0; padding: 0; }
  html, body {
    width: 1200px; height: 864px; overflow: hidden;
    background: var(--backdrop);
  }
  .canvas { position: relative; width: 1200px; height: 864px; }
  .card {
    position: absolute; width: 560px; height: 320px;
    background: var(--card); overflow: hidden;
  }
  .card--front { left: 220px; top: 90px; }
  .card--back { left: 420px; top: 454px; }

  .brand-word {
    font-family: "Asap Condensed", "Arial Narrow", sans-serif;
    font-weight: 500; color: var(--ink); letter-spacing: 0.5px;
  }
  .front-mark {
    position: absolute; left: 50%; top: 56px;
    width: 86px; height: 86px; margin-left: -43px;
    background: var(--brand-blue);
  }
  .front-name {
    position: absolute; left: 0; right: 0; top: 160px;
    text-align: center; font-size: 46px;
  }

  .back-name { position: absolute; left: 30px; top: 22px; font-size: 42px; }
  .back-decor {
    position: absolute; right: 30px; top: 40px;
    width: 250px; height: 250px; background: var(--pale-blue);
  }
  .person { position: absolute; left: 40px; top: 126px; font-family: "Open Sans", Arial, sans-serif; }
  .person__name { color: var(--brand-blue); font-weight: 700; font-size: 17px; line-height: 20px; }
  .person__title { color: var(--ink); font-size: 13px; line-height: 15px; }

  .contacts {
    position: absolute; left: 30px; top: 186px; list-style: none;
    font-family: "Open Sans", Arial, sans-serif; font-size: 14px;
    color: var(--ink); line-height: 19px;
  }
  .contacts li { display: flex; align-items: center; gap: 9px; }
  .contacts svg { width: 12px; height: 12px; fill: var(--brand-blue); flex: none; }
</style>
</head>
<body>
<main class="canvas">
  <section class="card card--front" aria-label="Business card front">
    <div class="front-mark"></div>
    <div class="front-name brand-word">RM Cargoline</div>
  </section>

  <section class="card card--back" aria-label="Business card back">
    <div class="back-decor"></div>
    <div class="back-name brand-word">RM Cargoline</div>
    <div class="person">
      <div class="person__name">Berki Zsófia</div>
      <div class="person__title">general manager</div>
    </div>
    <ul class="contacts">
      <li><svg viewBox="0 0 12 12" aria-hidden="true"><path d="M2.5 1l2 2.2-1 1.3c.7 1.5 2 2.8 3.5 3.5l1.3-1 2.2 2-1.2 1.8C5 10.5 1.5 7 .8 2.2z"/></svg>+36-70/482-5193</li>
      <li><svg viewBox="0 0 12 12" aria-hidden="true"><path d="M3 1h5v3H3zM1 5h10v5H1zm2 1.5v1h2v-1z"/></svg>+36-1/534-9061</li>
      <li><svg viewBox="0 0 12 12" aria-hidden="true"><path d="M1 2.5h10v7H1zm1 1v.4L6 6.5l4-2.6v-.4z"/></svg>zsofia.berki@rmcargoline.example</li>
      <li><svg viewBox="0 0 12 12" aria-hidden="true"><path d="M1 2.5h10v7H1zm1 1v.4L6 6.5l4-2.6v-.4z"/></svg>info@rmcargoline.example</li>
      <li><svg viewBox="0 0 12 12" aria-hidden="true"><path d="M5 7L7 5M4.3 5.7L3 7a1.4 1.4 0 002 2l1.3-1.3M7.7 6.3L9 5a1.4 1.4 0 00-2-2L5.7 4.3" stroke="#4f7fbf" stroke-width="1.3" fill="none"/></svg>www.rmcargoline.example</li>
    </ul>
  </section>
</main>
</body>
</html>
```